Summer Music/Chorus/Choir Camp for Young Singers Ages 8-13

We need a flyer for a summer camp for young singers ages 8-13. We are nonprofit community children's chorus in Miami, FL. Our camp provides specialized training in music theory, sight-reading,and aural training through daily choral rehearsals in an environment that is both positive and a lot of fun! Our camp offers children the opportunity to come as they are, no matter the level of experience, and grow tremendously in their musicianship skills. In addition to this, our campers participate in song-writing, masterclasses, community performances, and media projects. The final design should be clean, fun, not too crowded, should appeal to boys and girls ages 8-13, and something someone that age would consider "cool" and not too childish. Drawings are cool, something different.
Updates

Target Market(s)

Ages 8-13 and parents of those kids.

Industry/Entity Type

Community

Requirements
Must have
• All info attached.
Nice to have
• Things that relate to music, especially related to singing/choirs
Should not have
• instruments, stock photos of children, or photos from our website (unless they are used very creatively), or photos in general. I've attached our previous camp flyer and our current organization flyer but I don't necessarily want this flyer to look like those.

```html
<!DOCTYPE html>
<html lang="en">
<head>
<meta charset="utf-8">
<title>Summer Choral Camp Flyer</title>
<link rel="stylesheet" href="https://fonts.googleapis.com/css2?family=Oswald:wght@600;700&family=Roboto+Condensed:wght@700&family=Lato:ital,wght@0,700;1,700&family=Open+Sans:wght@400;700&display=swap">
<style>
  :root {
    --page-bg: #ece9e4;
    --header-dark: #454545;
    --header-mid: #5f5f5f;
    --ice: #c6e6e8;
    --teal: #5b9a96;
    --teal-deep: #1b7a7a;
    --teal-light: #cbe8ea;
    --teal-pale: #e0f1f2;
    --ink: #222;
    --ink-soft: #333;
    --grey-box: #7a7a7a;
    --rule: #1e1e1e;
    --white: #fff;
  }
  * { box-sizing: border-box; margin: 0; padding: 0; }
  html, body { width: 1200px; height: 902px; overflow: hidden; background: var(--page-bg); }
  .flyer {
    position: absolute; left: 30px; top: 45px; width: 1140px; height: 811px;
    background: var(--white); overflow: hidden;
    box-shadow: 0 6px 24px rgba(0,0,0,.25);
    font-family: 'Open Sans', sans-serif; color: var(--ink-soft);
  }
  .header {
    position: absolute; left: 0; top: 0; width: 100%; height: 168px;
    background: linear-gradient(90deg, var(--header-dark), var(--header-mid) 50%, var(--header-dark));
    text-align: center; font-family: 'Oswald', sans-serif; font-weight: 700;
    text-transform: uppercase; line-height: 1;
  }
  .header .invite { position: absolute; left: 0; right: 0; top: 38px; font-size: 50px; color: var(--white); letter-spacing: .5px; }
  .header .register { position: absolute; left: 0; right: 0; top: 103px; font-size: 50px; color: var(--ice); letter-spacing: .5px; }
  .header-strip { position: absolute; left: 0; top: 168px; width: 100%; height: 6px; background: var(--ice); }

  .hero-art { position: absolute; left: 0; top: 174px; width: 280px; height: 637px; }

  .about { position: absolute; left: 213px; top: 194px; width: 900px; }
  .about h2 { font-size: 16px; font-weight: 700; color: var(--teal-deep); text-transform: uppercase; }
  .about p { margin: 6px 0 0 3px; width: 893px; font-size: 14.5px; line-height: 19px; text-align: justify; color: var(--ink-soft); }

  .details { position: absolute; left: 277px; top: 296px; width: 863px; }
  .details-tab {
    width: 282px; height: 34px; background: #1a1a1a; color: var(--white);
    border-radius: 34px 34px 0 0; font-weight: 700; font-size: 16px;
    text-transform: uppercase; line-height: 36px; padding-left: 70px;
  }
  .row { display: flex; margin-bottom: 7px; }
  .row .label {
    width: 176px; display: flex; align-items: center; justify-content: center;
    font-family: 'Roboto Condensed', sans-serif; font-weight: 700; font-size: 19px; color: var(--ink);
    background: var(--teal-light);
  }
  .row .value { flex: 1; padding: 0 20px 0 15px; font-family: 'Lato', sans-serif; font-weight: 700; display: flex; flex-direction: column; justify-content: center; }
  .row-dates { height: 92px; }
  .row-dates .value { background: var(--teal); color: var(--white); }
  .row-dates .main { font-size: 38px; line-height: 1.1; }
  .row-dates .note { font-style: italic; font-size: 17px; margin-top: 2px; }
  .row-location { height: 77px; }
  .row-location .label { background: linear-gradient(90deg, var(--white), #f1f1f1); }
  .row-location .value { background: var(--teal-light); color: var(--ink-soft); font-size: 19px; line-height: 25px; padding-right: 60px; }
  .row-cost { height: 51px; }
  .row-cost .value { background: var(--teal); color: var(--white); font-size: 18px; }

  .org-name {
    position: absolute; left: 320px; top: 575px; width: 190px;
    font-family: 'Lato', sans-serif; font-weight: 700; font-size: 30px; line-height: 1.05;
    color: var(--teal); display: flex; align-items: center; gap: 10px;
  }
  .org-name .dot { width: 14px; height: 14px; border-radius: 50%; background: var(--teal); flex: none; }

  .contact { position: absolute; left: 568px; top: 582px; width: 572px; height: 109px; display: flex; }
  .contact .heading {
    width: 138px; background: var(--grey-box); color: var(--white);
    font-family: 'Roboto Condensed', sans-serif; font-weight: 700; font-size: 19px; line-height: 23px;
    display: flex; align-items: center; justify-content: center; text-align: center;
  }
  .contact .info { flex: 1; background: var(--teal-pale); padding: 12px 0 0 30px; font-family: 'Roboto Condensed', sans-serif; font-weight: 700; color: #2a2a2a; }
  .contact .phone { font-size: 36px; line-height: 42px; letter-spacing: .5px; }
  .contact .email { font-size: 22px; margin-top: 10px; }

  .footer-rule { position: absolute; left: 268px; top: 711px; width: 872px; height: 3px; background: var(--rule); }
  .sponsors { position: absolute; left: 312px; top: 730px; width: 820px; height: 66px; display: flex; align-items: center; }
  .sponsor { font-family: 'Open Sans', sans-serif; font-weight: 700; color: var(--rule); display: flex; align-items: center; gap: 6px; }
  .sponsor-fund { font-size: 17px; }
  .sponsor-county { font-size: 11px; margin-left: 20px; width: 60px; line-height: 1.1; }
  .sponsor .square { width: 12px; height: 12px; background: var(--rule); flex: none; }
  .badge { width: 62px; height: 62px; border: 3px solid var(--rule); margin-left: 22px; flex: none; }
  .nonprofit-note { margin-left: 22px; width: 420px; font-size: 11px; line-height: 15px; color: #333; }
</style>
</head>
<body>
  <main class="flyer">
    <header class="header">
      <h1 class="invite">Singers in Grades 3-9 are invited to attend!</h1>
      <p class="register">Register Today!</p>
    </header>
    <div class="header-strip"></div>

    <svg class="hero-art" viewBox="0 0 280 637" role="img" aria-label="Photo of a young boy holding a microphone toward the viewer over a pale teal panel of musical notes">
      <defs>
        <linearGradient id="heroFill" x1="0" y1="0" x2="0" y2="1">
          <stop offset="0" stop-color="#9fd6d8"/>
          <stop offset=".45" stop-color="#c3e6e7"/>
          <stop offset="1" stop-color="#e4f2f2"/>
        </linearGradient>
      </defs>
      <path d="M0 0 H172 C 225 150, 262 380, 268 637 H0 Z" fill="url(#heroFill)"/>
      <path d="M172 0 C 225 150, 262 380, 268 637" fill="none" stroke="#1e1e1e" stroke-width="8"/>
    </svg>

    <section class="about">
      <h2>About Our Camp</h2>
      <p>Youth and children who love to sing will have a blast at our choral camp! Our music educators and industry professionals are dedicated to enhancing the lives of young singers through choral training which develops vocal technique, ear-training, music reading, and interpersonal skills. Activities are fun and interactive and former music training is not necessary.</p>
    </section>

    <section class="details">
      <div class="details-tab">Camp Details</div>
      <div class="row row-dates">
        <div class="label">Dates and Times</div>
        <div class="value">
          <span class="main">July 18-29, 9am-3pm (M-F)*</span>
          <span class="note">*Extended hours available (7:30am-5:30pm) for an extra $50 per week.</span>
        </div>
      </div>
      <div class="row row-location">
        <div class="label">Location</div>
        <div class="value">Southside Cultural Arts Center, 4820 SW 180th Street Miami, FL 33187</div>
      </div>
      <div class="row row-cost">
        <div class="label">Cost</div>
        <div class="value">*$300 for 2-week session &nbsp;, &nbsp;&nbsp;*Price does not include lunch.</div>
      </div>
    </section>

    <div class="org-name"><span class="dot"></span><span>Bright Notes Chorus</span></div>

    <section class="contact">
      <div class="heading">Our Contact<br>information</div>
      <div class="info">
        <div class="phone">305.555.0148</div>
        <div class="email">info@brightnoteschorus.org</div>
      </div>
    </section>

    <div class="footer-rule"></div>
    <footer class="sponsors">
      <span class="sponsor sponsor-fund"><span class="square"></span>Harbor Arts Fund</span>
      <span class="sponsor sponsor-county">Bayline County</span>
      <span class="badge" aria-label="Partner badge"></span>
      <p class="nonprofit-note">Bright Notes Chorus is a 501 (c)(3) Nonprofit organization. Donations made to BNC are tax-exempt.</p>
    </footer>
  </main>
</body>
</html>
```